Layout für Longboardshop
Zielgruppe
Online Shop für Longboards, basierend auf Ladenwerk 4.1.2
Zielgruppe: Sportliche Menschen mit Hang zum Wellenreiten, Surfen,Kiten, Snowboarden oder Skateboarden.
Aufgabenstellung
Erstellung des Grunddesigns (Header, Footer, Menü, Detailansicht, Buttons) als PSD. Die Umsetzung in ein Template erledigen wir alleine.
Neugründung: Es existieren noch keine Logos oder Farbvorgaben.
We have no site, it is a completly new project. There are no limits concerning colors, fonts etc.
Competitors:
http://www.brettfahrer-welt.de
http://wilhelmine-bretter.de/
http://www.rollbrettladen.de/
http://www.kavero.de/de_DE/Skateboard/Longboards.html?sid=1
http://www.pirumo-bretter.de/
I think, big pictures transporting the surfstyle attitude of this sport works good.
Der Grundaufbau sollte sich an http://www.ladenwerkdemo.de/ anlehnen, um den Anpassungsaufwand mgl. überschaubar zu halten.

```html
<!DOCTYPE html>
<html lang="de">
<head>
<meta charset="utf-8">
<title>Wellenbrett – Longboard Shop</title>
<link href="https://fonts.googleapis.com/css2?family=Source+Sans+3:ital,wght@0,400;0,600;0,700;1,400&display=swap" rel="stylesheet">
<style>
:root{
  --bg:#e3e3e3;
  --topbar:#1a6c9c;
  --brand:#1a7ca6;
  --brand-dark:#13628a;
  --teal:#1e94b3;
  --btn-dark:#1a6893;
  --accent:#1b9cc6;
  --ink:#1e1e1e;
  --muted:#4a4a4a;
  --footer:#232323;
  --white:#ffffff;
}
*{box-sizing:border-box;margin:0;padding:0}
html,body{width:1200px;height:1140px;overflow:hidden}
body{font-family:"Source Sans 3",Arial,sans-serif;background:var(--bg);color:var(--ink)}
.canvas{position:relative;width:1200px;height:1140px;overflow:hidden;background:radial-gradient(ellipse at 50% 40%,#ececec,#dcdcdc)}
.abs{position:absolute}

/* top bar */
.topbar{left:0;top:0;width:1200px;height:25px;background:var(--topbar);border-top:2px solid #13557c}
.topnav{left:485px;top:0;height:25px;display:flex}
.topnav .item{display:flex;align-items:center;gap:6px;padding:0 10px;height:23px;color:#fff;font-size:8.5px;border-left:1px solid rgba(255,255,255,.18)}
.topnav .item:last-child{border-right:1px solid rgba(255,255,255,.18)}
.flag{width:13px;height:9px;background:linear-gradient(#111 0 33%,#d00 33% 66%,#f5c400 66%)}
.search{left:840px;top:6px;width:120px;height:15px;background:#fff;border-radius:8px;font-size:7px;font-style:italic;color:#888;padding:2px 0 0 13px}
.search svg{position:absolute;right:8px;top:4px}

/* logo */
.logo{left:249px;top:18px;width:176px;height:82px}
.logo-name{left:249px;top:22px;width:176px;text-align:center;color:#fff;font-weight:700;font-size:20px;line-height:1;letter-spacing:1px}

/* seal */
.seal{left:668px;top:52px;display:flex;align-items:center;gap:5px}
.seal-mark{width:22px;height:22px;border-radius:50%;background:#4d4d4d;border:2px solid #c9c9c9}
.seal-text{font-size:6.5px;line-height:9px;color:#777}
.seal-text b{color:#666}

/* cart */
.cart{left:790px;top:41px;width:170px;height:55px;background:#fff}
.cart-head{height:38px;display:flex;align-items:center;padding-left:34px;gap:10px;border-bottom:1px solid #e2e2e2}
.cart-label{font-size:8.5px;font-weight:600;letter-spacing:.3px;margin-left:4px}
.cart-count{width:17px;height:17px;border-radius:50%;background:var(--brand-dark);color:#fff;font-size:8px;display:flex;align-items:center;justify-content:center;margin-left:10px}
.cart-info{font-size:7.5px;text-align:center;padding-top:3px}
.cart-info u{font-weight:600}

/* nav + hero panel */
.hero-panel{left:240px;top:137px;width:720px;height:240px;background:#fff}
.nav{left:240px;top:114px;width:720px;height:23px;background:linear-gradient(#1e8fb2,#15729a)}
.nav-home{left:240px;top:109px;width:68px;height:28px;background:#fff}
.nav-home span{position:absolute;left:9px;top:7px;width:51px;height:19px;border:1px solid var(--brand);color:var(--brand);font-size:8.5px;font-weight:600;display:flex;align-items:center;justify-content:center;letter-spacing:.4px}
.nav-item{top:114px;height:23px;color:#fff;font-size:8.5px;font-weight:600;letter-spacing:.4px;display:flex;align-items:center;justify-content:center;transform:translateX(-50%)}
.nav-sep{top:114px;width:1px;height:23px;background:rgba(0,0,0,.18)}
.hero-main{left:258px;top:156px;width:473px;height:199px;background:radial-gradient(ellipse at 30% 40%,#6cc3e6,#1b7bb5 55%,#0d4f86)}
.hero-copy{right:481px;top:236px;text-align:right;color:#fff;font-weight:700;line-height:.82;letter-spacing:-1.5px}
.hero-copy .big{font-size:46px}
.hero-copy .mid{font-size:34px}
.hero-side1{left:739px;top:156px;width:200px;height:95px;background:linear-gradient(#1e5e86,#6aa3bd 55%,#e8d9a4 75%,#1d3f5a)}
.hero-side2{left:739px;top:259px;width:200px;height:96px;background:linear-gradient(#8b6a8f,#e58a5a 50%,#f5c27a)}
.panel-shadow{left:262px;top:376px;width:676px;height:5px;border-radius:50%;background:radial-gradient(ellipse,rgba(0,0,0,.35),transparent 70%)}

/* product panels */
.panel{background:#fff}
.products{display:flex}
.product{position:absolute;width:150px;transform:translateX(-50%);text-align:center}
.product-img{margin:0 auto;width:90px;border-radius:40px}
.title{font-size:11.5px;font-weight:600;letter-spacing:-.1px;line-height:13px}
.desc,.price{font-size:7.5px;color:var(--ink);line-height:11px}
.price b{font-weight:700}
.btns{display:flex;justify-content:center;gap:3px;margin-top:7px}
.btn{height:20px;display:flex;align-items:center;justify-content:center;color:#fff;font-size:7.5px;font-weight:600;letter-spacing:.2px}
.btn.details{width:40px;background:var(--btn-dark)}
.btn.cart-add{width:85px;background:var(--teal)}
.vert{left:251px;top:458px;width:10px;color:#fff;font-size:10.5px;font-weight:700;line-height:11.6px;text-align:center;word-break:break-all}

.tab{left:265px;top:660px;width:101px;height:26px;background:#fff}
.tab span{position:absolute;left:10px;top:4px;width:81px;height:19px;border:1px solid var(--brand);color:var(--brand);font-size:8.5px;font-weight:600;display:flex;align-items:center;justify-content:center;letter-spacing:.3px}
.arrow-col{top:685px;width:24px;height:252px;background:linear-gradient(90deg,#1a80a8,#136d97);display:flex;align-items:center;justify-content:center}

/* footer */
.footer-band{left:0;top:996px;width:1200px;height:8px;background:var(--accent)}
.footer{left:0;top:1004px;width:1200px;height:136px;background:var(--footer)}
.footer-line{left:0;top:1137px;width:1200px;height:3px;background:var(--topbar)}
.hex{left:579px;top:980px}
.f-head{top:1029px;font-size:8.5px;color:#fff;letter-spacing:.1px}
.f-head em{font-style:normal;color:var(--accent)}
.f-list{top:1056px;font-size:8px;color:#fff;line-height:15.7px}
.f-list a{color:var(--accent);text-decoration:none}
.f-text{left:751px;top:1056px;width:212px;font-size:8px;color:#fff;line-height:15.7px}
</style>
</head>
<body>
<div class="canvas">

  <!-- top bar -->
  <div class="abs topbar"></div>
  <nav class="abs topnav">
    <div class="item"><svg width="9" height="9" viewBox="0 0 10 10"><circle cx="5" cy="3" r="2.4" fill="#fff"/><path d="M0 10c0-3 2-4.5 5-4.5s5 1.5 5 4.5z" fill="#fff"/></svg>Mein Konto</div>
    <div class="item"><svg width="9" height="11" viewBox="0 0 9 11"><rect x=".7" y="1.5" width="7.6" height="9" fill="none" stroke="#fff" stroke-width="1.2"/><rect x="2.5" y="0" width="4" height="2.5" fill="#fff"/><path d="M2.5 6l1.5 1.5 3-3" fill="none" stroke="#fff"/></svg>Merkzettel</div>
    <div class="item"><svg width="11" height="11" viewBox="0 0 11 11"><path d="M1 1l9 9M10 1L1 10" stroke="#fff" stroke-width="1.8"/></svg>Service/Hilfe</div>
    <div class="item"><svg width="7" height="5" viewBox="0 0 7 5"><path d="M0 0l3.5 4L7 0" fill="none" stroke="#fff" stroke-width="1.5"/></svg>&nbsp;EUR</div>
    <div class="item"><svg width="7" height="5" viewBox="0 0 7 5"><path d="M0 0l3.5 4L7 0" fill="none" stroke="#fff" stroke-width="1.5"/></svg><span class="flag"></span></div>
  </nav>
  <div class="abs search">Suchbegriff<svg width="7" height="7" viewBox="0 0 7 7"><circle cx="3" cy="3" r="2.2" fill="none" stroke="#aaa"/><path d="M4.6 4.6L6.6 6.6" stroke="#aaa"/></svg></div>

  <!-- logo area -->
  <svg class="abs logo" viewBox="0 0 176 82" aria-hidden="true">
    <path d="M3 0H173L170 48L88 80L6 48Z" fill="#1a7ca6"/>
    <path d="M11 0H165L162 43L88 72L14 43Z" fill="#208fb6"/>
  </svg>
  <div class="abs logo-name">WELLEN<br>BRETT</div>

  <div class="abs seal"><span class="seal-mark"></span><div class="seal-text"><b>Sicher</b> einkaufen<br>Siegelpartner zertifiziert</div></div>

  <div class="abs cart">
    <div class="cart-head">
      <svg width="20" height="26" viewBox="0 0 20 26"><path d="M6 7V4a4 4 0 0 1 8 0v3" fill="none" stroke="#2a78b4" stroke-width="1.3"/><path d="M1 7h18l-1 19H2z" fill="#2a78b4"/></svg>
      <span class="cart-label">WARENKORB</span>
      <span class="cart-count">2</span>
    </div>
    <div class="cart-info">Es befinden sich <u>2 Artikel</u> im Warenkorb.</div>
  </div>

  <!-- navigation + hero -->
  <div class="abs hero-panel"></div>
  <div class="abs nav"></div>
  <div class="abs nav-home"><span>HOME</span></div>
  <div class="abs nav-item" style="left:363px">DECKS</div>
  <div class="abs nav-sep" style="left:415px"></div>
  <div class="abs nav-item" style="left:470px">ZUBEHÖR</div>
  <div class="abs nav-sep" style="left:526px"></div>
  <div class="abs nav-item" style="left:579px">% SALE</div>
  <div class="abs nav-sep" style="left:632px"></div>
  <div class="abs nav-item" style="left:675px">TEAM</div>
  <div class="abs nav-sep" style="left:722px"></div>
  <div class="abs nav-item" style="left:776px">BILDER</div>
  <div class="abs nav-sep" style="left:831px"></div>
  <div class="abs nav-item" style="left:894px">KONTAKT</div>

  <div class="abs hero-main" role="img" aria-label="Surfbrett von unten in einer blauen Welle"></div>
  <div class="abs hero-copy"><div class="big">-10%</div><div class="mid">AUF ALLE<br>BOARDS</div></div>
  <div class="abs hero-side1" role="img" aria-label="Skater als Silhouette vor Abendhimmel"></div>
  <div class="abs hero-side2" role="img" aria-label="Springender Skater im orangen Gegenlicht"></div>
  <div class="abs panel-shadow"></div>

  <!-- topseller -->
  <div class="abs panel" style="left:240px;top:388px;width:720px;height:251px"></div>
  <svg class="abs" style="left:240px;top:388px" width="36" height="251" viewBox="0 0 36 251" aria-hidden="true">
    <defs><linearGradient id="stripe" x1="0" x2="1"><stop offset="0" stop-color="#13689a"/><stop offset="1" stop-color="#1c8fb5"/></linearGradient></defs>
    <path d="M0 0H24L35 125L24 251H0Z" fill="url(#stripe)"/>
  </svg>
  <div class="abs vert">TOPSELLER</div>

  <div class="product" style="left:357px;top:401px">
    <div class="product-img" role="img" aria-label="Longboard-Deck mit bunter Grafik, Ober- und Unterseite" style="height:149px;background:linear-gradient(90deg,#3c3f45 0 45%,transparent 45% 55%,#4a9cb5 55%)"></div>
    <div class="title" style="margin-top:19px">ARTIKELBEZEICHNUNG</div>
    <div class="desc">Lorem Ipsum. Proin gravidanv.</div>
    <div class="price">Preis: <b>123,00€</b> inkl. MwSt.</div>
    <div class="btns"><span class="btn details">DETAILS</span><span class="btn cart-add">IN DEN WARENKORB</span></div>
  </div>
  <div class="product" style="left:518px;top:401px">
    <div class="product-img" role="img" aria-label="Bambus-Longboard mit illustrierter Unterseite" style="height:149px;background:linear-gradient(90deg,#c79a66 0 45%,transparent 45% 55%,#a88c6a 55%)"></div>
    <div class="title" style="margin-top:19px">ARTIKELBEZEICHNUNG</div>
    <div class="desc">Lorem Ipsum. Proin gravidanv.</div>
    <div class="price">Preis: <b>123,00€</b> inkl. MwSt.</div>
    <div class="btns"><span class="btn details">DETAILS</span><span class="btn cart-add">IN DEN WARENKORB</span></div>
  </div>
  <div class="product" style="left:684px;top:401px">
    <div class="product-img" role="img" aria-label="Schwarzes Longboard mit goldener Grafik" style="height:149px;background:linear-gradient(90deg,#3a3a3a 0 45%,transparent 45% 55%,#6b5a3c 55%)"></div>
    <div class="title" style="margin-top:19px">ARTIKELBEZEICHNUNG</div>
    <div class="desc">Lorem Ipsum. Proin gravidanv.</div>
    <div class="price">Preis: <b>123,00€</b> inkl. MwSt.</div>
    <div class="btns"><span class="btn details">DETAILS</span><span class="btn cart-add">IN DEN WARENKORB</span></div>
  </div>
  <div class="product" style="left:849px;top:401px">
    <div class="product-img" role="img" aria-label="Longboard in Grün, Gelb und Rot" style="height:149px;background:linear-gradient(#3f9a5b,#c9b23c 50%,#c8463a)"></div>
    <div class="title" style="margin-top:19px">ARTIKELBEZEICHNUNG</div>
    <div class="desc">Lorem Ipsum. Proin gravidanv.</div>
    <div class="price">Preis: <b>123,00€</b> inkl. MwSt.</div>
    <div class="btns"><span class="btn details">DETAILS</span><span class="btn cart-add">IN DEN WARENKORB</span></div>
  </div>

  <!-- alle artikel -->
  <div class="abs tab"><span>ALLE ARTIKEL</span></div>
  <div class="abs panel" style="left:240px;top:685px;width:720px;height:252px"></div>
  <div class="abs arrow-col" style="left:240px"><svg width="6" height="10" viewBox="0 0 6 10"><path d="M5 1L1 5l4 4" fill="none" stroke="#fff" stroke-width="1.6"/></svg></div>
  <div class="abs arrow-col" style="left:936px"><svg width="6" height="10" viewBox="0 0 6 10"><path d="M1 1l4 4-4 4" fill="none" stroke="#fff" stroke-width="1.6"/></svg></div>

  <div class="product" style="left:353px;top:696px">
    <div class="product-img" role="img" aria-label="Silberne Longboard-Achse" style="width:125px;height:152px;border-radius:0;background:radial-gradient(ellipse 50% 14% at 50% 50%,#b8b8b8,transparent)"></div>
    <div class="title" style="margin-top:20px">ARTIKELBEZEICHNUNG</div>
    <div class="desc">Lorem Ipsum. Proin gravidanv.</div>
    <div class="price">Preis: <b>123,00€</b> inkl. MwSt.</div>
    <div class="btns"><span class="btn details">DETAILS</span><span class="btn cart-add">IN DEN WARENKORB</span></div>
  </div>
  <div class="product" style="left:518px;top:696px">
    <div class="product-img" role="img" aria-label="Bambus-Longboard mit illustrierter Unterseite" style="height:152px;background:linear-gradient(90deg,#c79a66 0 45%,transparent 45% 55%,#a88c6a 55%)"></div>
    <div class="title" style="margin-top:20px">ARTIKELBEZEICHNUNG</div>
    <div class="desc">Lorem Ipsum. Proin gravidanv.</div>
    <div class="price">Preis: <b>123,00€</b> inkl. MwSt.</div>
    <div class="btns"><span class="btn details">DETAILS</span><span class="btn cart-add">IN DEN WARENKORB</span></div>
  </div>
  <div class="product" style="left:685px;top:696px">
    <div class="product-img" role="img" aria-label="Schwarzes Longboard mit goldener Grafik" style="height:152px;background:linear-gradient(90deg,#3a3a3a 0 45%,transparent 45% 55%,#6b5a3c 55%)"></div>
    <div class="title" style="margin-top:20px">ARTIKELBEZEICHNUNG</div>
    <div class="desc">Lorem Ipsum. Proin gravidanv.</div>
    <div class="price">Preis: <b>123,00€</b> inkl. MwSt.</div>
    <div class="btns"><span class="btn details">DETAILS</span><span class="btn cart-add">IN DEN WARENKORB</span></div>
  </div>
  <div class="product" style="left:847px;top:696px">
    <div class="product-img" role="img" aria-label="Weiße Longboard-Rolle mit schwarzer Grafik" style="width:100px;height:152px;border-radius:0;background:radial-gradient(circle 50px at 50% 50%,#e9e9e9 0 60%,#555 80%,transparent 81%)"></div>
    <div class="title" style="margin-top:20px">ARTIKELBEZEICHNUNG</div>
    <div class="desc">Lorem Ipsum. Proin gravidanv.</div>
    <div class="price">Preis: <b>123,00€</b> inkl. MwSt.</div>
    <div class="btns"><span class="btn details">DETAILS</span><span class="btn cart-add">IN DEN WARENKORB</span></div>
  </div>

  <!-- footer -->
  <div class="abs footer-band"></div>
  <footer class="abs footer"></footer>
  <svg class="abs hex" width="42" height="40" viewBox="0 0 42 40" aria-hidden="true">
    <path d="M21 1L40 10V30L21 39L2 30V10Z" fill="#1b9cc6" stroke="#137aa0" stroke-width="2"/>
  </svg>
  <div class="abs f-head" style="left:239px"><em>WELLENBRETT</em> SITEMAP</div>
  <div class="abs f-head" style="left:454px"><em>WELLENBRETT</em> KONTAKT</div>
  <div class="abs f-head" style="left:749px"><em>WELLENBRETT</em> VERSANDINFOS</div>

  <div class="abs f-list" style="left:239px">Home<br>Decks<br>Zubehör<br>Sale</div>
  <div class="abs f-list" style="left:283px">Team<br>Bilder<br>Kontakt<br>AGB</div>
  <div class="abs f-list" style="left:326px">Mein Konto<br>Datenschutz<br>Merkzettel<br>Impressum</div>
  <div class="abs f-list" style="left:454px">Wellenbrett GmbH<br>Brandungsweg 1<br>12345 Wellenstadt<br>Deutschland</div>
  <div class="abs f-list" style="left:562px">T: 04821 - 55 30 17 20<br>F: 04821 - 55 30 17 21<br>M: <a>info@wellenbrett-shop.de</a><br>W: <a>www.wellenbrett-shop.de</a></div>
  <div class="abs f-text">Lorem Ipsum. Proin gravida nibh vel velit auctor aliquet. Aenean sollicitudin, lorem quis bibendum auctor, nisi elit consequat ipsum, nec sagittis sem nibh id elit. Duis sed odio sit amet nibh vulputate cursus a sit amet mauris.</div>
  <div class="abs footer-line"></div>
</div>
</body>
</html>
```